Landing Page IT Security Vendor

We need a landing page that uses our colour scheme (www.veldonguard.com). We created a draft (see attached). We do not need standard stock template design pages. Please only apply if you can design pages from scratch and try to be as close as possible to our draft. It is ok to also purchase commecrial stock pictures

Coding

Coded - Design and coding required

Number of Pages Required

1 page

```html
<!DOCTYPE html>
<html lang="en">
<head>
<meta charset="utf-8">
<title>Veldon Guard – Security Awareness</title>
<link href="https://fonts.googleapis.com/css2?family=Open+Sans:wght@300;400;600;700&display=swap" rel="stylesheet">
<style>
:root{
  --teal:#14b0b7;
  --teal-dark:#0ea2a9;
  --orange:#fbab1e;
  --orange-text:#f5a31a;
  --ice:#b4e5ef;
  --ice-soft:#dff3f8;
  --grey-band:#8e8e8e;
  --ink:#1a1a1a;
  --white:#ffffff;
}
*{margin:0;padding:0;box-sizing:border-box}
html,body{width:1200px;height:2204px;overflow:hidden}
body{font-family:"Open Sans",sans-serif;color:var(--ink);background:var(--white);position:relative}
.abs{position:absolute}
.hero{left:0;top:0;width:1200px;height:651px;background:var(--teal)}
.hero-photo{left:600px;top:86px;width:600px;height:522px;background:radial-gradient(ellipse at 75% 45%,#e9d6c4 0%,#9fd6d6 40%,rgba(20,176,183,0) 72%)}
.awards{top:30px;left:45px;display:flex;gap:30px}
.award{display:flex;align-items:center;gap:8px;color:#fff;font-size:10px;line-height:14px;font-weight:300;width:290px}
.award svg{flex:none}
.nav-home{left:959px;top:24px;width:92px;height:38px;border-radius:19px;background:#9fe0e0;color:#fff;font-size:18px;font-weight:300;display:flex;align-items:center;justify-content:center}
.nav-sol{left:1072px;top:31px;color:#fff;font-size:18px;font-weight:300}
.kicker{left:45px;top:136px;color:#fff;font-size:31px;font-weight:300;letter-spacing:.3px}
.headline{left:45px;top:212px;color:#fff;font-size:50px;font-weight:700;line-height:66px;letter-spacing:.5px}
.btn{background:var(--orange);color:#fff;border-radius:40px;display:flex;align-items:center;justify-content:center;font-weight:600}
.demo{left:710px;top:210px;width:253px;height:66px;font-size:21px}
.help{left:44px;top:490px;color:#fff;font-size:27px;font-weight:700}
.ice{left:0;top:651px;width:1200px;height:490px;background:var(--ice-soft)}
.panel{top:576px;width:377px;height:565px;background:linear-gradient(#c9ecf3 0%,#e9f7fa 30%,#eef9fb 80%,var(--ice) 92%)}
.card{top:609px;width:328px;height:461px;background:#fff;border:8px solid #eef8fa;padding:30px 30px}
.card h3{color:var(--orange-text);font-size:21px;font-weight:700;line-height:29px;text-transform:uppercase;margin-bottom:18px}
.card .lead{font-size:13px;font-weight:600;line-height:22px;margin-bottom:14px}
.card p{font-size:13px;font-weight:400;line-height:22px;color:#333}
.card .btn{position:absolute;left:30px;bottom:34px;width:252px;height:54px;font-size:19px}
.mssp{left:0;top:1141px;width:1200px;height:83px;background:var(--grey-band);color:#fff;font-size:21px;font-weight:600;display:flex;align-items:center;justify-content:center}
.mssp a{color:var(--orange);text-decoration:underline;margin-left:6px}
.trust h2{font-size:32px;font-weight:600;line-height:40px}
.trust h2 span{color:var(--orange)}
.trust p{font-size:15px;line-height:24px;margin-top:14px;color:#222}
.contact-btn{left:45px;top:1602px;width:535px;height:65px;font-size:21px}
.logos{left:664px;top:1287px;width:494px;height:405px;background:#fff;border:6px solid #f2f4f4}
.logo{position:absolute;display:flex;align-items:center;gap:8px;font-weight:700;font-size:22px}
.logo i{display:block;width:26px;height:26px;flex:none}
.footer{left:0;top:1755px;width:1200px;height:449px;background:var(--teal);color:#fff}
.footer h4{font-size:21px;font-weight:700}
.col{font-size:16px;line-height:23.5px}
.rule{left:45px;top:2045px;width:1110px;height:1px;background:#7fd4d8}
.badge{top:2093px;width:62px;height:62px;background:rgba(255,255,255,.25);border-radius:8px}
.badge.round{border-radius:50%}
</style>
</head>
<body>
<section class="abs hero">
  <div class="abs hero-photo" role="img" aria-label="Smiling woman holding a tablet over faint technology line icons"></div>
  <div class="abs awards">
    <div class="award"><svg width="22" height="22" viewBox="0 0 22 22"><path d="M5 3h12v5a6 6 0 0 1-12 0z M9 15h4v3h3v2H6v-2h3z" fill="#fff"/></svg>In 2020, VELDON won the Secure Merit Award for Best "Anti Phishing"</div>
    <div class="award"><svg width="30" height="22" viewBox="0 0 30 22"><circle cx="15" cy="11" r="9" fill="none" stroke="#fff" stroke-width="2"/><path d="M15 6l1.5 3.5 3.5.3-2.7 2.3.9 3.6L15 13.8l-3.2 1.9.9-3.6L10 9.8l3.5-.3z" fill="#fff"/></svg>In 2020, VELDON won the Secure Merit Award for Best "Security Education Platform"</div>
    <div class="award"><svg width="26" height="22" viewBox="0 0 26 22"><circle cx="13" cy="11" r="9" fill="none" stroke="#fff" stroke-width="2"/><text x="13" y="15" fill="#fff" font-size="10" text-anchor="middle" font-family="Open Sans,sans-serif">1</text></svg>2020 Gold Winner "Cyber Security Education and Training" in the SecTech Buyers Digest</div>
  </div>
  <div class="abs nav-home">Home</div>
  <div class="abs nav-sol">Solution ⌄</div>
  <div class="abs kicker">CYBER SECURITY STARTS WITH PEOPLE</div>
  <h1 class="abs headline">TRAIN YOUR STAFF WITH<br>VELDON AND IMPROVE CYBER<br>SECURITY AWARENESS</h1>
  <div class="abs btn demo">Request a demo</div>
  <div class="abs help">HOW CAN WE HELP?</div>
</section>

<div class="abs ice"></div>
<div class="abs panel" style="left:21px"></div>
<div class="abs panel" style="left:412px"></div>
<div class="abs panel" style="left:802px"></div>
<svg class="abs" style="left:0;top:550px" width="1200" height="60" viewBox="0 0 1200 60">
  <path d="M210 60V5H988V60 M598 5V55" fill="none" stroke="#fff" stroke-width="2" stroke-dasharray="2 4"/>
</svg>

<div class="abs card" style="left:45px">
  <h3>Import our training courses in your LMS</h3>
  <div class="lead">Buy out of the box or custom tailored security courses you can import in your e-learning (SCORM)</div>
  <p>VELDON offers 250 fully customizable training modules in +30 languages. Games, videos, exams, posters, offline, micro-training and much more!</p>
  <div class="btn">Explore Our Training</div>
</div>
<div class="abs card" style="left:437px">
  <h3>Let us develop a security awareness program</h3>
  <div class="lead">Veldon Guard will assist you in improving security awareness - with money back guarantee!</div>
  <p>Our security awareness specialists will identify risky users via phishing simulations. We develop a tailored awareness program and reduce your exposure to social hacking.</p>
  <div class="btn">Explore Our Services</div>
</div>
<div class="abs card" style="left:827px">
  <h3>Install the Veldon software on-premise or get access to the SaaS version</h3>
  <div class="lead">You want to run the campaign yourself? Choose your preferred setup type and get started in 24h!</div>
  <p>The VELDON software can be installed on-premise or in the cloud. If you don’t want to deal with the installation we onboard you in 24h on our SaaS!</p>
  <div class="btn">Explore Our Software</div>
</div>

<div class="abs mssp">VELDON is also available for MSSP - <a>Learn More</a></div>

<section class="abs trust" style="left:45px;top:1304px;width:560px">
  <h2>Already over <span>12,000,000</span> Employees worldwide trust and use VELDON</h2>
  <p style="margin-top:28px">Veldon Guard is a name you can trust! Becuase we have won countless awrds since 2015 and help well-known brands around the world.</p>
  <p>Youknow you’re getting a quality solution with us.</p>
  <p>Our services can be customized to fit youro needs and company size. Talk to our tram today to learn more.</p>
</section>
<div class="abs btn contact-btn">Get in Contact with the VELDON Team Now!</div>

<div class="abs logos">
  <div class="logo" style="left:28px;top:40px;color:#1a3b8c"><i style="background:#1a3b8c"></i>Norvia</div>
  <div class="logo" style="left:170px;top:40px;color:#e30613">Railor</div>
  <div class="logo" style="left:300px;top:40px;color:#e30613"><i style="background:#e30613"></i>Hausfeld</div>
  <div class="logo" style="left:28px;top:130px;color:#d0021b"><i style="background:#d0021b;border-radius:50%"></i>Kestrel Tools</div>
  <div class="logo" style="left:300px;top:130px;color:#1f3c88">Alpwing</div>
  <div class="logo" style="left:28px;top:210px;color:#006e63"><i style="background:#006e63"></i>Mahlberg</div>
  <div class="logo" style="left:250px;top:210px;color:#1a2a5a">Tessin Informatik</div>
  <div class="logo" style="left:28px;top:300px;color:#222">Chemvale</div>
  <div class="logo" style="left:230px;top:300px;color:#333;font-size:18px;font-weight:400">Spreetal Stadtdienste<i style="background:#f26b1d"></i></div>
</div>

<footer class="abs footer">
  <h4 class="abs" style="left:45px;top:42px">CONTACTS</h4>
  <h4 class="abs" style="left:998px;top:42px">LANGUAGE</h4>
  <div class="abs col" style="left:45px;top:97px">Address: Europe<br>Veldon Guard AG<br>Lindenweg 12 | 6301 Baar | Switzerland</div>
  <div class="abs col" style="left:405px;top:97px">Address: North America<br>Veldon Guard USA<br>4410 Harbor View Dr<br>Suite 210<br>Denton, TX 76201</div>
  <div class="abs col" style="left:653px;top:97px">Phone Global: +41 44 000 12 34<br>Phone USA: +1-555-010-2200<br>Phone USA Support: +1-555-010-2211<br>Phone France: +33 600 000 142<br>Phone UK: +44 (0) 7000 111222</div>
  <div class="abs col" style="left:998px;top:97px">English ⌄</div>
</footer>
<div class="abs rule"></div>
<div class="abs" style="left:45px;top:2098px;color:#fff;font-size:18px;font-weight:700">Veldon</div>
<div class="abs" style="left:45px;top:2136px;color:#fff;font-size:16px">All Rights Reserved 2020</div>
<div class="abs badge" style="left:265px"></div>
<div class="abs badge round" style="left:367px"></div>
<div class="abs badge" style="left:452px"></div>
<div class="abs badge" style="left:526px"></div>
<div class="abs badge" style="left:601px"></div>
<div class="abs badge" style="left:682px;width:92px;height:40px;top:2104px"></div>
<div class="abs badge" style="left:796px"></div>
<div class="abs badge" style="left:880px"></div>
<div class="abs badge" style="left:980px;width:88px;height:36px;top:2106px"></div>
<div class="abs badge round" style="left:1094px"></div>
</body>
</html>
```